Horse related business entrepreneur needs a business card

I need a business card design for my horse related business. The enterprise is Copper Fen LLC and I have 3 businesses (headquartered at 2 locations): 1. property management where we rent horse stalls and apartments at a thoroughbred training center outside Ocala; 2. a medium sized transportation service in central Florida that sells horse bedding and removes used horse bedding from horse farms; and horse racing

```html
<!DOCTYPE html>
<html lang="en">
<head>
<meta charset="utf-8">
<title>Copper Fen LLC — Business Card</title>
<link rel="stylesheet" href="https://fonts.googleapis.com/css2?family=Lato:wght@400;700&family=Raleway:wght@600&display=swap">
<style>
  :root {
    --canvas: #e9e6e1;
    --card-dark: #262627;
    --card-light: #ffffff;
    --teal: #2a9177;
    --text-dark: #2a2a2a;
    --text-light: #f2f2f2;
    --wordmark-light: #d9d9d9;
  }
  * { margin: 0; padding: 0; box-sizing: border-box; }
  html, body { width: 1200px; height: 900px; overflow: hidden; }
  body {
    background: var(--canvas);
    position: relative;
    font-family: "Lato", Arial, sans-serif;
  }
  .card {
    position: absolute;
    left: 280px;
    width: 640px;
    height: 366px;
    border-radius: 4px;
    overflow: hidden;
    box-shadow: 0 6px 18px rgba(0,0,0,0.18);
  }
  /* Back of card */
  .card-back { top: 56px; background: var(--card-dark); }
  .card-back .wordmark {
    position: absolute;
    left: 0; right: 0; top: 150px;
    display: flex; align-items: center; justify-content: center; gap: 16px;
    font-family: "Raleway", Arial, sans-serif;
    font-weight: 600;
    font-size: 46px;
    color: var(--wordmark-light);
    letter-spacing: 0.5px;
  }
  .wordmark .dot {
    width: 26px; height: 26px; border-radius: 50%;
    background: var(--teal);
  }
  /* Front of card */
  .card-front { top: 478px; background: var(--card-light); }
  .card-front .wave { position: absolute; inset: 0; width: 100%; height: 100%; }
  .holder { position: absolute; left: 52px; top: 44px; }
  .holder-name { font-weight: 700; font-size: 30px; color: var(--teal); line-height: 1.1; }
  .holder-role { font-size: 17px; color: var(--text-dark); margin-left: 10px; margin-top: 2px; }
  .contact-list {
    position: absolute; left: 58px; top: 146px;
    list-style: none; font-size: 19px; color: var(--text-dark); line-height: 1.25;
  }
  .contact-list li { display: flex; align-items: center; gap: 8px; }
  .contact-list svg { width: 16px; height: 16px; fill: var(--teal); flex: none; }
  .address-main {
    position: absolute; left: 76px; top: 232px;
    font-size: 20px; color: var(--text-dark); line-height: 1.2;
  }
  .card-front .wordmark {
    position: absolute; left: 350px; top: 86px; width: 260px;
    display: flex; align-items: center; justify-content: center; gap: 12px;
    font-weight: 700; font-size: 30px; color: var(--teal);
  }
  .card-front .wordmark .dot { width: 18px; height: 18px; }
  .address-alt {
    position: absolute; right: 28px; top: 238px;
    text-align: right; font-size: 15px; color: var(--text-light); line-height: 1.3;
  }
</style>
</head>
<body>

<section class="card card-back">
  <div class="wordmark"><span class="dot"></span><span>Copper Fen LLC</span></div>
</section>

<section class="card card-front">
  <svg class="wave" viewBox="0 0 640 366" preserveAspectRatio="none" aria-hidden="true">
    <path d="M0 366 L0 318 C250 350 380 270 480 190 C545 154 600 142 640 140 L640 366 Z" fill="var(--teal)"/>
    <path d="M0 366 L0 334 C250 366 380 286 480 206 C545 170 600 158 640 156 L640 366 Z" fill="#ffffff"/>
    <path d="M0 366 L0 342 C250 374 380 294 480 214 C545 178 600 166 640 164 L640 366 Z" fill="var(--card-dark)"/>
  </svg>

  <div class="holder">
    <div class="holder-name">Owen Harlow</div>
    <div class="holder-role">Owner</div>
  </div>

  <ul class="contact-list">
    <li>
      <svg viewBox="0 0 16 16"><path d="M3.5 1.5l2.5 0 1.2 3-1.6 1.2a9 9 0 0 0 4.7 4.7l1.2-1.6 3 1.2v2.5a1.5 1.5 0 0 1-1.6 1.5A12.5 12.5 0 0 1 2 3.1 1.5 1.5 0 0 1 3.5 1.5z"/></svg>
      (352) 555-0148
    </li>
    <li>
      <svg viewBox="0 0 16 16"><path d="M4 1h8v4H4z M2 6h12a1 1 0 0 1 1 1v5h-3v3H4v-3H1V7a1 1 0 0 1 1-1z M5.5 10.5v3h5v-3z"/></svg>
      (352) 555-0193
    </li>
    <li>
      <svg viewBox="0 0 16 16"><path d="M1 3h14v10H1z M2 4.2v.6l6 4.2 6-4.2v-.6z" fill-rule="evenodd"/></svg>
      owen@copperfen.com
    </li>
  </ul>

  <div class="address-main">1240 SE 92nd Lane<br>Dunnellon, FL 34431</div>

  <div class="wordmark"><span class="dot"></span><span>Copper Fen LLC</span></div>

  <div class="address-alt">718 Willow Creek Road<br>Ocala, FL 34482</div>
</section>

</body>
</html>
```